Talvina Moreau R&B Mixtape CD Cover

We need a cd cover for an r&b mixtape. The artist's name is Talvina Moreau and the name of the mixtape is 4:17. The cover should reflect a vibe of 4:17 am in the morning where a young female has concluded clubbing and the night is left open ended, meaning it could be the beginning of a whole new morning or the night not ending. The cover should be creative and reflect the essence of a breakout artist. The cover will be used as the visual for all online music posts i.e. tunevault, beatharbr, echoplatform, etc. Artist name and the title of the mixtape should be included on the cover.

Target Market(s)

R&B music lovers aged 19-39.

Industry/Entity Type

Music Download

Requirements
Must have
• Reflecting of time and having a good time.

```html
<!DOCTYPE html>
<html lang="en">
<head>
<meta charset="utf-8">
<title>Talvina Moreau – 4:17</title>
<link rel="stylesheet" href="https://fonts.googleapis.com/css2?family=Orbitron:wght@700&family=Crimson+Text:wght@700&display=swap">
<style>
  :root {
    --night: #0d0006;
    --night-deep: #050002;
    --neon: #e0138f;
    --neon-soft: #f07ac4;
    --neon-glow: rgba(240, 40, 170, 0.75);
  }
  html, body {
    margin: 0;
    padding: 0;
    width: 1200px;
    height: 1200px;
    overflow: hidden;
    background: var(--night);
  }
  .cover {
    position: relative;
    width: 1200px;
    height: 1200px;
    overflow: hidden;
    background: var(--night);
  }
  .street-photo {
    position: absolute;
    inset: 0;
    background:
      linear-gradient(122deg, rgba(0,0,0,0) 0%, rgba(0,0,0,0) 38%, var(--night) 58%),
      linear-gradient(200deg, var(--night-deep) 0%, #6d0a47 55%, var(--neon) 80%, #8a1060 100%);
  }
  .clock {
    position: absolute;
    left: 530px;
    top: 150px;
    margin: 0;
    font-family: "Orbitron", sans-serif;
    font-weight: 700;
    font-size: 220px;
    line-height: 1;
    letter-spacing: 6px;
    color: var(--neon-soft);
    text-shadow: 0 0 6px var(--neon), 0 0 22px var(--neon-glow), 0 0 44px var(--neon-glow);
  }
  .artist-block {
    position: absolute;
    left: 474px;
    top: 893px;
    width: 636px;
  }
  .dot-rule {
    display: block;
    width: 636px;
    height: 8px;
  }
  .artist-name {
    margin: 30px 0 34px;
    text-align: center;
    font-family: "Crimson Text", serif;
    font-weight: 700;
    font-size: 72px;
    line-height: 1;
    letter-spacing: 1px;
    text-transform: uppercase;
    color: var(--neon);
  }
</style>
</head>
<body>
  <main class="cover">
    <div class="street-photo" role="img" aria-label="Night street scene: a young woman walking away along a neon-pink lit sidewalk, her long shadow stretching across the pavement"></div>

    <h1 class="clock">4:17</h1>

    <div class="artist-block">
      <svg class="dot-rule" viewBox="0 0 636 8" aria-hidden="true">
        <line x1="4" y1="4" x2="632" y2="4" stroke="var(--neon)" stroke-width="6" stroke-linecap="round" stroke-dasharray="0 10.3"/>
      </svg>
      <p class="artist-name">Talvina Moreau</p>
      <svg class="dot-rule" viewBox="0 0 636 8" aria-hidden="true">
        <line x1="4" y1="4" x2="632" y2="4" stroke="var(--neon)" stroke-width="6" stroke-linecap="round" stroke-dasharray="0 10.3"/>
      </svg>
    </div>
  </main>
</body>
</html>
```